PowerPoint Template Design for business consulting company in Silicon Valley

I need a PowerPoint template to use as the starting point for new presentations. I have a logo but now need design that supports this. I've attached a very descriptive PDF that explains exactly what I need. Here is a list of deliverables: 1. PowerPoint Template that I will use as the starter presentation for all new Vantor Bellway presentationsDesigns for the following slides: See picture below for examples of structure:2. Title slide with subtitle3. Section header4. Title and body5. Title and 2 columns6. Title and 3 columns7. One column text8. Editable timeline to show months, or steps for a process9. Bullet design for unordered list (can be graphic)10. Bullet design for ordered list11. Recommended fonts for each design: Title, subtitle, list, captionOPTIONAL: Possible graphic elements to be used for section title slide backgrounds or graphic elements:--Your team / my team / people on project--Goals for project / presentation--Editable Timeline--Speaking--Writing--Listening--People collaborating / helping each otherI am happy to accept proposals for developing these optional elements in a separate project.

Requirements
Must have
• Must be FLAT design.
• Not flashy or garish. Must be subtle.

```html
<!DOCTYPE html>
<html lang="en">
<head>
<meta charset="utf-8">
<title>Vantor Bellway – Presentation Template</title>
<link href="https://fonts.googleapis.com/css2?family=Questrial&display=swap" rel="stylesheet">
<style>
:root{
  --bg:#e6e6f7;
  --white:#ffffff;
  --green:#1f7a45;
  --green-light:#46b568;
  --blue:#22449b;
  --blue-mid:#4a5fb0;
  --blue-soft:#5d7fd8;
  --ink:#1d1d1d;
  --muted:#666;
  --tile:#d9d9d9;
  --grad:linear-gradient(90deg,var(--green),var(--blue));
}
*{margin:0;padding:0;box-sizing:border-box}
html,body{width:1200px;height:443px;overflow:hidden;background:var(--bg);font-family:"Questrial",Arial,sans-serif;color:var(--ink)}
.canvas{position:relative;width:1200px;height:443px}
.slide{position:absolute;width:222px;height:125px;background:var(--white);overflow:hidden}
.abs{position:absolute}
.mark{position:absolute;left:10px;top:0;width:5px;height:14px;background:linear-gradient(180deg,var(--blue),var(--green))}
.footbar{position:absolute;right:0;bottom:4px;height:3px;width:72%;background:linear-gradient(90deg,var(--green) 0 20%,var(--blue))}
.title{position:absolute;left:18px;top:10px;font-size:8.5px;color:var(--ink)}
.photo{position:absolute}
.tiny{font-size:3.6px;line-height:1.3;color:var(--muted)}
.head-blue{color:var(--blue);font-size:6px;line-height:1.05}
/* slide specific */
.cover-photo{inset:0;background:linear-gradient(180deg,#6fa5b4 0%,#4e7b86 45%,#5b6b55 70%,#c36b7e 100%)}
.cover-frame{left:9px;top:7px;width:146px;height:110px;border:1px solid rgba(255,255,255,.85)}
.cover-title{left:12px;top:14px;color:#fff;font-size:15px;line-height:1.15}
.agenda-list{left:18px;top:35px;font-size:4px;line-height:1.3}
.agenda-list b{font-size:5.2px}
.col-box{top:30px;width:45px;height:70px;color:#fff;font-size:3.3px;line-height:1.3;padding:20px 3px 0}
.band{left:0;top:68px;width:222px;height:57px;background:var(--grad)}
.band-title{left:10px;top:88px;color:#fff;font-size:11px}
.stat-label{color:var(--blue);font-size:6.5px;line-height:1}
.stat-val{color:var(--green);font-size:11px;display:flex;align-items:baseline;gap:1px}
.stat-val small{font-size:3.5px}
.quote{inset:0;background:var(--grad);color:#fff;text-align:center}
.team-band{left:0;top:52px;width:222px;height:73px;background:var(--grad)}
.member{top:44px;width:31px;color:#fff}
.member .pic{height:24px;background:linear-gradient(160deg,#8c8c8c,#c7c7c7)}
.member b{display:block;font-size:3.4px;margin-top:3px}
.member .tiny{color:#d8e2f4;font-size:2.8px}
.loc{width:58px;height:33px;background:linear-gradient(180deg,#7ea4c9,#5d7a8f)}
.loc span{position:absolute;left:0;bottom:2px;width:100%;background:rgba(255,255,255,.88);font-size:4.3px;color:var(--blue);padding:1px 3px}
</style>
</head>
<body>
<main class="canvas">

<!-- 1 Title slide -->
<section class="slide" style="left:27px;top:25px">
  <div class="photo cover-photo" role="img" aria-label="Photo of a pagoda on a hillside with blossoming trees"></div>
  <div class="abs cover-frame"></div>
  <h1 class="abs cover-title" style="font-weight:400">SLIDE<br>TITLE</h1>
</section>

<!-- 2 Agenda list -->
<section class="slide" style="left:258px;top:25px">
  <div class="mark"></div>
  <h2 class="abs" style="left:62px;top:14px;font-size:8.5px;font-weight:400">Agenda</h2>
  <div class="abs agenda-list">
    <b>1.Company</b><br>&nbsp;&nbsp;1. Company profile<br>&nbsp;&nbsp;2. Core competence<br>&nbsp;&nbsp;3. Philosophy<br>&nbsp;&nbsp;4. History<br>&nbsp;&nbsp;5. Milestones<br>&nbsp;&nbsp;6. Key figures<br>
    <b>2.Structures</b><br>&nbsp;&nbsp;1. Team<br>&nbsp;&nbsp;2. Employees<br>&nbsp;&nbsp;3. Locations
  </div>
  <div class="photo" style="left:97px;top:0;width:125px;height:125px;background:linear-gradient(180deg,#6fa5b4,#5b6b55 65%,#c36b7e)" role="img" aria-label="Photo of a pagoda on a hillside"></div>
</section>

<!-- 3 Agenda columns -->
<section class="slide" style="left:489px;top:25px">
  <div class="mark"></div>
  <h2 class="title" style="font-weight:400">Agenda</h2>
  <div class="abs col-box" style="left:8px;background:var(--green)">1. COMPANY<br>2. COMPANY PROFILE<br>3. CORE COMPETENCE<br>4. PHILOSOPHY<br>4. HISTORY<br>5. MILESTONES<br>6. KEY FIGURES</div>
  <div class="abs col-box" style="left:61px;background:var(--green-light)">2. STRUCTURES<br>1. TEAM<br>2. EMPLOYEES<br>3. LOCATIONS</div>
  <div class="abs col-box" style="left:114px;background:var(--blue-mid)">3. PORTFOLIO<br>1. PRODUCTS<br>2. SERVICES<br>3. CLIENTS<br>4. PARTNERS<br>5. PRICES</div>
  <div class="abs col-box" style="left:167px;background:var(--blue-soft)">4. REFERENCE<br>1. TESTIMONIALS<br>2. PRIVACY POLICY<br>3. SUMMARY<br>4. Q&amp;A<br>5. CONTACT<br>INFORMATION</div>
  <div class="footbar"></div>
</section>

<!-- 4 Specialists -->
<section class="slide" style="left:720px;top:25px">
  <div class="mark"></div>
  <p class="abs tiny" style="left:10px;top:8px;width:95px;color:#333">Lorem ipsum dolor sit amet, consectetur adipiscing elit, sed do eiusmod tempor incididunt ut labore et dolore magna aliqua. Ut enim ad minim veniam, quis nostrud exercitation ullamco laboris nisi ut aliquip ex ea commodo consequat. Duis aute irure dolor in</p>
  <p class="abs tiny" style="left:115px;top:8px;width:95px;color:#333">reprehenderit in voluptate velit esse cillum dolore eu fugiat nulla pariatur. Excepteur sint occaecat cupidatat non proident, sunt in culpa qui officia deserunt mollit anim id est laborum.</p>
  <div class="abs band"></div>
  <svg class="abs" style="left:10px;top:68px" width="10" height="6" viewBox="0 0 10 6"><path d="M0 0H10L5 6Z" fill="#fff"/></svg>
  <h2 class="abs band-title" style="font-weight:400">WE ARE THE SPECIALISTS</h2>
</section>

<!-- 5 Company profile -->
<section class="slide" style="left:951px;top:25px">
  <div class="mark"></div>
  <h2 class="abs" style="left:22px;top:17px;font-size:7px;font-weight:400">Company profile</h2>
  <div class="abs" style="left:10px;top:33px;width:205px;display:grid;grid-template-columns:1fr 1fr 1fr;row-gap:6px">
    <div><div class="stat-label">TOTAL ASSETS</div><div class="stat-val" style="margin-top:4px"><svg width="8" height="6" viewBox="0 0 8 6"><path d="M0 6L3 3L4.5 4.5L8 0M5.5 0H8V2.5" stroke="#1f7a45" stroke-width="1.2" fill="none"/></svg>$520<small>million</small></div></div>
    <div><div class="stat-label">NET INCOME</div><div class="stat-val" style="margin-top:4px"><svg width="8" height="6" viewBox="0 0 8 6"><path d="M0 6L3 3L4.5 4.5L8 0M5.5 0H8V2.5" stroke="#1f7a45" stroke-width="1.2" fill="none"/></svg>$442<small>million</small></div></div>
    <div><div class="stat-label">REVENUE</div><div class="stat-val" style="margin-top:4px"><svg width="8" height="6" viewBox="0 0 8 6"><path d="M0 6L3 3L4.5 4.5L8 0M5.5 0H8V2.5" stroke="#1f7a45" stroke-width="1.2" fill="none"/></svg>$256<small>million</small></div></div>
    <div><div class="stat-label">LOANS</div><div class="stat-val" style="margin-top:9px"><svg width="8" height="6" viewBox="0 0 8 6"><path d="M0 6L3 3L4.5 4.5L8 0M5.5 0H8V2.5" stroke="#1f7a45" stroke-width="1.2" fill="none"/></svg>$100<small>million</small></div></div>
    <div><div class="stat-label">DEPOSITS</div><div class="stat-val" style="margin-top:9px"><svg width="8" height="6" viewBox="0 0 8 6"><path d="M0 6L3 3L4.5 4.5L8 0M5.5 0H8V2.5" stroke="#1f7a45" stroke-width="1.2" fill="none"/></svg>$232<small>million</small></div></div>
    <div><div class="stat-label">TOTAL TAXES<br>PAID</div><div class="stat-val" style="margin-top:2px"><svg width="8" height="6" viewBox="0 0 8 6"><path d="M0 6L3 3L4.5 4.5L8 0M5.5 0H8V2.5" stroke="#1f7a45" stroke-width="1.2" fill="none"/></svg>$521<small>million</small></div></div>
  </div>
  <div class="footbar"></div>
</section>

<!-- 6 Quote -->
<section class="slide" style="left:27px;top:159px">
  <div class="abs quote">
    <div style="font-size:22px;line-height:1;margin-top:22px;font-family:Georgia,serif">&ldquo;</div>
    <p style="font-size:5px;line-height:1.35">THE FUTURE BELONGS<br>TO THOSE WHO SEE POSSIBILITIES<br>BEFORE THEY BECOME OBVIOUS.</p>
    <div style="font-size:22px;line-height:.8;margin-top:4px;font-family:Georgia,serif">&rdquo;</div>
    <p style="font-size:5px;margin-top:2px">CEO</p>
  </div>
</section>

<!-- 7 Our values grid -->
<section class="slide" style="left:258px;top:159px">
  <div class="mark"></div>
  <h2 class="title" style="font-weight:400;font-size:8px">Our values</h2>
  <div class="abs" style="left:18px;top:32px;width:48px"><div class="head-blue">INNOVATION</div><p class="tiny" style="margin-top:2px">Lorem ipsum dolor sit amet, consectetur adipiscing elit, sed do eiusmod tempor</p></div>
  <div class="abs" style="left:18px;top:72px;width:48px"><div class="head-blue">THE BEST OF ALL AREAS</div><p class="tiny" style="margin-top:2px">Lorem ipsum dolor sit amet, consectetur adipiscing elit, sed do eiusmod tempor</p></div>
  <div class="abs" style="left:165px;top:32px;width:50px"><div class="head-blue">GOOD DEALS</div><p class="tiny" style="margin-top:2px">Lorem ipsum dolor sit amet, consectetur adipiscing elit, sed do eiusmod tempor</p></div>
  <div class="abs" style="left:165px;top:76px;width:50px"><div class="head-blue">SECURITY</div><p class="tiny" style="margin-top:2px">Lorem ipsum dolor sit amet, consectetur adipiscing elit, sed do eiusmod tempor</p></div>
  <div class="photo" style="left:76px;top:30px;width:33px;height:33px;background:linear-gradient(135deg,#4a4a4a,#b8b8b8)" role="img" aria-label="Photo of people stacking hands"></div>
  <div class="photo" style="left:117px;top:30px;width:33px;height:33px;background:linear-gradient(135deg,#d7d7d7,#6d6d6d)" role="img" aria-label="Photo of a business handshake"></div>
  <div class="photo" style="left:76px;top:71px;width:33px;height:33px;background:linear-gradient(135deg,#3c5f9a,#c9cdd6)" role="img" aria-label="Photo of a man in a suit"></div>
  <div class="photo" style="left:117px;top:71px;width:33px;height:33px;background:linear-gradient(135deg,#e3e3e3,#7f8792)" role="img" aria-label="Photo of a handshake over a desk"></div>
  <div class="footbar"></div>
</section>

<!-- 8 Our values photo -->
<section class="slide" style="left:489px;top:159px">
  <div class="mark"></div>
  <h2 class="title" style="font-weight:400;font-size:8px;top:18px">Our values</h2>
  <p class="abs tiny" style="left:10px;top:37px;width:100px;color:#333">Lorem ipsum dolor sit amet, consectetur adipiscing elit, sed do eiusmod tempor</p>
  <p class="abs" style="left:11px;top:48px;color:var(--blue);font-size:7px;line-height:1.3">Trust<br>Honesty<br>Respect.</p>
  <div class="photo" style="left:115px;top:0;width:107px;height:125px;background:linear-gradient(160deg,#6b4a32,#3e3a3a 55%,#23304a)" role="img" aria-label="Photo of hands typing on a laptop"></div>
  <div class="abs" style="left:0;top:91px;width:117px;height:27px;background:var(--grad)"></div>
  <p class="abs tiny" style="left:12px;top:97px;width:95px;color:#fff">Lorem ipsum dolor sit amet, consectetur adipiscing elit, sed do eiusmod tempor</p>
</section>

<!-- 9 Milestones bar -->
<section class="slide" style="left:720px;top:159px">
  <div class="mark"></div>
  <h2 class="title" style="font-weight:400;font-size:8px;top:16px">Milestones</h2>
  <div class="abs" style="left:10px;top:33px;width:200px;display:flex;gap:10px">
    <div style="flex:1;border-left:.5px solid #999;padding-left:2px;height:30px"><div class="head-blue" style="font-size:4.3px">FOUNDATION OF THE COMPANY</div><p class="tiny" style="font-size:3px;margin-top:2px">This is a placeholder text</p></div>
    <div style="flex:1;border-left:.5px solid #999;padding-left:2px;height:30px"><div class="head-blue" style="font-size:4.3px">NEW BUSINESS BRANCH</div><p class="tiny" style="font-size:3px;margin-top:2px">This is a placeholder text</p></div>
    <div style="flex:1;border-left:.5px solid #999;padding-left:2px;height:30px"><div class="head-blue" style="font-size:4.3px">NEW MANAGING DIRECTOR</div><p class="tiny" style="font-size:3px;margin-top:2px">This is a placeholder text</p></div>
  </div>
  <svg class="abs" style="left:10px;top:64px" width="205" height="7" viewBox="0 0 205 7">
    <defs><linearGradient id="tl" x1="0" x2="1"><stop offset="0" stop-color="#1f7a45"/><stop offset="1" stop-color="#22449b"/></linearGradient></defs>
    <path d="M0 0H200L205 3.5L200 7H0Z" fill="url(#tl)"/>
  </svg>
  <div class="abs" style="left:13px;top:65px;width:190px;display:flex;justify-content:space-between;color:#fff;font-size:3.6px">
    <span>1990</span><span>1995</span><span>2000</span><span>2005</span><span>2006</span><span>2007</span><span>2010</span><span>2012</span><span>2016</span><span>2018</span><span>Vision</span>
  </div>
  <div class="abs" style="left:40px;top:74px;width:175px;display:flex;gap:10px">
    <div style="flex:1;border-left:.5px solid #999;padding-left:2px;padding-top:12px;height:30px"><div class="head-blue" style="font-size:4.3px">GRAND OPENING: NY OFFICE</div><p class="tiny" style="font-size:3px;margin-top:2px">This is a placeholder text</p></div>
    <div style="flex:1;border-left:.5px solid #999;padding-left:2px;padding-top:12px;height:30px"><div class="head-blue" style="font-size:4.3px">NUMBER OF EMPLOYEES RISES</div><p class="tiny" style="font-size:3px;margin-top:2px">This is a placeholder text</p></div>
    <div style="flex:1;border-left:.5px solid #999;padding-left:2px;padding-top:12px;height:30px"><div class="head-blue" style="font-size:4.3px">OUR VISION</div><p class="tiny" style="font-size:3px;margin-top:2px">This is a placeholder text</p></div>
  </div>
  <div class="footbar"></div>
</section>

<!-- 10 Milestones dotted -->
<section class="slide" style="left:951px;top:159px">
  <div class="mark"></div>
  <h2 class="title" style="font-weight:400;font-size:8px;top:18px">Milestones</h2>
  <svg class="abs" style="left:0;top:0" width="222" height="125" viewBox="0 0 222 125" font-family="Questrial, Arial, sans-serif">
    <line x1="12" y1="67" x2="207" y2="67" stroke="#1f6f7a" stroke-width=".6" stroke-dasharray="1.5 1.5"/>
    <path d="M205 65L208 67L205 69" stroke="#1f6f7a" stroke-width=".6" fill="none"/>
    <g stroke="#9aa" stroke-width=".4">
      <line x1="12" y1="38" x2="12" y2="67"/><line x1="29" y1="48" x2="29" y2="67"/><line x1="80" y1="38" x2="80" y2="67"/>
      <line x1="114" y1="50" x2="114" y2="67"/><line x1="152" y1="38" x2="152" y2="67"/><line x1="181" y1="50" x2="181" y2="67"/>
      <line x1="29" y1="67" x2="29" y2="92"/><line x1="63" y1="67" x2="63" y2="98"/><line x1="97" y1="67" x2="97" y2="82"/>
      <line x1="131" y1="67" x2="131" y2="98"/><line x1="165" y1="67" x2="165" y2="82"/>
    </g>
    <g fill="#1f6f7a"><circle cx="12" cy="67" r="1"/><circle cx="29" cy="67" r="1"/><circle cx="63" cy="67" r="1"/><circle cx="80" cy="67" r="1"/><circle cx="97" cy="67" r="1"/><circle cx="114" cy="67" r="1"/><circle cx="131" cy="67" r="1"/><circle cx="152" cy="67" r="1"/><circle cx="165" cy="67" r="1"/><circle cx="181" cy="67" r="1"/></g>
    <g font-size="5" fill="#22449b">
      <text x="11" y="36">2000</text><text x="31" y="50">2004</text><text x="82" y="36">2008</text><text x="116" y="52">2013</text><text x="154" y="36">2016</text><text x="183" y="52">2020</text>
      <text x="31" y="95">2002</text><text x="65" y="101">2006</text><text x="99" y="85">2011</text><text x="133" y="101">2015</text><text x="167" y="85">2018</text>
      <text x="185" y="70" font-size="4.3">Future</text>
    </g>
    <g font-size="3" fill="#888">
      <text x="14" y="41">This is a placeholder text</text><text x="31" y="54">This is a place</text><text x="31" y="57.5">holder text</text>
      <text x="82" y="41">This is a place</text><text x="82" y="44.5">holder text</text><text x="116" y="56">This is a place</text><text x="116" y="59.5">holder text</text>
      <text x="154" y="41">This is a place</text><text x="154" y="44.5">holder text</text><text x="183" y="56">This is a place</text><text x="183" y="59.5">holder text</text>
      <text x="31" y="99">This is a place</text><text x="31" y="102.5">holder text</text><text x="65" y="105">This is a placeholder text</text>
      <text x="99" y="89">This is a place</text><text x="99" y="92.5">holder text</text><text x="133" y="105">This is a placeholder text</text>
      <text x="167" y="89">This is a place</text><text x="167" y="92.5">holder text</text>
    </g>
  </svg>
  <div class="footbar"></div>
</section>

<!-- 11 Sales by region -->
<section class="slide" style="left:27px;top:293px">
  <div class="mark"></div>
  <h2 class="title" style="font-weight:400;font-size:7.5px;top:18px">Sales by region 2018</h2>
  <div class="photo" style="left:18px;top:30px;width:190px;height:80px;background:radial-gradient(ellipse at 50% 50%,#e8e8e8 0%,#f4f4f4 60%,#fff 100%)" role="img" aria-label="Faint world map"></div>
  <svg class="abs" style="left:0;top:0" width="222" height="125" viewBox="0 0 222 125" font-family="Questrial, Arial, sans-serif">
    <g fill="none" stroke-width="11" transform="rotate(-90 129 68)">
      <circle cx="129" cy="68" r="22" pathLength="155" stroke="#2b47a5" stroke-dasharray="70 85"/>
      <circle cx="129" cy="68" r="22" pathLength="155" stroke="#4a78e0" stroke-dasharray="40 115" stroke-dashoffset="-70"/>
      <circle cx="129" cy="68" r="22" pathLength="155" stroke="#1fa5ef" stroke-dasharray="20 135" stroke-dashoffset="-110"/>
      <circle cx="129" cy="68" r="22" pathLength="155" stroke="#8a8a8a" stroke-dasharray="15 140" stroke-dashoffset="-130"/>
      <circle cx="129" cy="68" r="22" pathLength="155" stroke="#d4d4d4" stroke-dasharray="10 145" stroke-dashoffset="-145"/>
    </g>
    <g fill="#fff" font-size="8" text-anchor="middle"><text x="155" y="71">70</text><text x="123" y="96">40</text><text x="106" y="74">20</text><text x="117" y="54" fill="#333" font-size="6">15</text><text x="130" y="47" fill="#333" font-size="5">10</text></g>
    <text x="129" y="66" font-size="3.3" fill="#2b47a5" text-anchor="middle">TOTAL SALES:</text>
    <text x="129" y="73" font-size="6" fill="#2b47a5" text-anchor="middle">$M</text>
    <g stroke="#999" stroke-width=".4"><line x1="56" y1="41" x2="120" y2="50"/><line x1="56" y1="47" x2="120" y2="50"/><line x1="56" y1="75" x2="108" y2="72"/><line x1="56" y1="96" x2="120" y2="92"/><line x1="166" y1="68" x2="188" y2="68"/></g>
    <rect x="16" y="39" width="40" height="5" fill="#9a9a9a"/><rect x="16" y="45" width="40" height="5" fill="#bdbdbd"/>
    <rect x="16" y="72" width="40" height="5" fill="#1f7a45"/><rect x="16" y="93" width="40" height="5" fill="#4a78e0"/>
    <rect x="185" y="66" width="30" height="5" fill="#2b47a5"/>
    <g font-size="3.2" fill="#fff"><text x="18" y="42.6">Placeholder</text><text x="18" y="48.6">Placeholder</text><text x="18" y="75.6">Placeholder</text><text x="18" y="96.6">Placeholder</text><text x="187" y="69.6">Placeholder</text></g>
    <text x="103" y="112" font-size="3.5" fill="#555">TEXT</text>
  </svg>
  <div class="footbar"></div>
</section>

<!-- 12 Your team -->
<section class="slide" style="left:258px;top:293px">
  <div class="mark"></div>
  <h2 class="title" style="font-weight:400;font-size:8px;top:18px">Your Team</h2>
  <div class="abs team-band"></div>
  <div class="abs member" style="left:10px"><div class="pic" role="img" aria-label="Team member portrait"></div><b>LINO VARO</b><p class="tiny">Job Description</p><p class="tiny" style="margin-top:2px">This is a placeholder text. This text can be replaced with your own text.</p></div>
  <div class="abs member" style="left:44px"><div class="pic" role="img" aria-label="Team member portrait"></div><b>MIRA TOSK</b><p class="tiny">Job Description</p><p class="tiny" style="margin-top:2px">This is a placeholder text. This text can be replaced with your own text.</p></div>
  <div class="abs member" style="left:78px"><div class="pic" role="img" aria-label="Team member portrait"></div><b>PIA RENN</b><p class="tiny">Job Description</p><p class="tiny" style="margin-top:2px">This is a placeholder text. This text can be replaced with your own text.</p></div>
  <div class="abs member" style="left:112px"><div class="pic" role="img" aria-label="Team member portrait"></div><b>PAUL OSTIN</b><p class="tiny">Job Description</p><p class="tiny" style="margin-top:2px">This is a placeholder text. This text can be replaced with your own text.</p></div>
  <div class="abs member" style="left:146px"><div class="pic" role="img" aria-label="Team member portrait"></div><b>DARA QUILL</b><p class="tiny">Job Description</p><p class="tiny" style="margin-top:2px">This is a placeholder text. This text can be replaced with your own text.</p></div>
  <div class="abs member" style="left:180px"><div class="pic" role="img" aria-label="Team member portrait"></div><b>MILO BRANT</b><p class="tiny">Job Description</p><p class="tiny" style="margin-top:2px">This is a placeholder text. This text can be replaced with your own text.</p></div>
</section>

<!-- 13 Our employees -->
<section class="slide" style="left:489px;top:293px">
  <div class="mark"></div>
  <h2 class="title" style="font-weight:400;font-size:8px;top:17px">Our employees</h2>
  <div class="abs" style="left:11px;top:28px;display:grid;grid-template-columns:repeat(13,13px);grid-auto-rows:13px;gap:3px">
    <i style="background:var(--tile)"></i><i style="background:var(--tile)"></i><i style="background:var(--tile)"></i><i style="background:var(--tile)"></i><i style="background:var(--tile)"></i><i style="background:var(--tile)"></i><i style="background:var(--tile)"></i><i style="background:var(--tile)"></i><i style="background:#9a8d84" role="img" aria-label="Employee portrait"></i><i style="background:#a89a8e" role="img" aria-label="Employee portrait"></i><i style="background:#8e8178" role="img" aria-label="Employee portrait"></i><i style="background:#b2a597" role="img" aria-label="Employee portrait"></i><i style="background:#9b8f86" role="img" aria-label="Employee portrait"></i>
    <i style="background:var(--tile)"></i><i style="background:var(--tile)"></i><i style="background:var(--tile)"></i><i style="background:var(--tile)"></i><i style="background:var(--tile)"></i><i style="background:var(--tile)"></i><i style="background:var(--tile)"></i><i style="background:var(--tile)"></i><i style="background:var(--tile)"></i><i style="background:var(--tile)"></i><i style="background:#a0938a" role="img" aria-label="Employee portrait"></i><i style="background:#b5a799" role="img" aria-label="Employee portrait"></i><i style="background:#8f847c" role="img" aria-label="Employee portrait"></i>
    <i style="background:var(--tile)"></i><i style="background:var(--tile)"></i><i style="background:var(--tile)"></i><i style="background:var(--tile)"></i><i style="background:var(--tile)"></i><i style="background:var(--tile)"></i><i style="background:var(--tile)"></i><i style="background:var(--tile)"></i><i style="background:var(--tile)"></i><i style="background:var(--tile)"></i><i style="background:var(--tile)"></i><i style="background:#a69a8f" role="img" aria-label="Employee portrait"></i><i style="background:#94887f" role="img" aria-label="Employee portrait"></i>
    <i style="background:var(--tile)"></i><i style="background:var(--tile)"></i><i style="background:var(--tile)"></i><i style="background:var(--tile)"></i><i style="background:var(--tile)"></i><i style="background:var(--tile)"></i><i style="background:var(--tile)"></i><i style="background:var(--tile)"></i><i style="background:var(--tile)"></i><i style="background:var(--tile)"></i><i style="background:var(--tile)"></i><i style="background:var(--tile)"></i><i style="background:#a3968b" role="img" aria-label="Employee portrait"></i>
    <i style="background:var(--tile)"></i><i style="background:var(--tile)"></i><i style="background:var(--tile)"></i><i style="background:var(--tile)"></i><i style="background:var(--tile)"></i><i style="background:var(--tile)"></i><i style="background:var(--tile)"></i><i style="background:var(--tile)"></i><i style="background:var(--tile)"></i><i style="background:var(--tile)"></i><i style="background:var(--tile)"></i><i style="background:var(--tile)"></i><i style="background:#998d85" role="img" aria-label="Employee portrait"></i>
  </div>
  <div class="footbar"></div>
</section>

<!-- 14 Business locations -->
<section class="slide" style="left:720px;top:293px">
  <div class="mark"></div>
  <h2 class="title" style="font-weight:400;font-size:7.5px;top:17px">Business locations</h2>
  <div class="abs loc" style="left:10px;top:33px" role="img" aria-label="City skyline photo"><span>Location a</span></div>
  <div class="abs loc" style="left:82px;top:33px;background:linear-gradient(180deg,#8fb3d6,#5f7384)" role="img" aria-label="City skyline photo"><span>Location B</span></div>
  <div class="abs loc" style="left:154px;top:33px;background:linear-gradient(180deg,#a6c1df,#6c7e8c)" role="img" aria-label="City skyline photo"><span>Location c</span></div>
  <div class="abs loc" style="left:10px;top:72px;background:linear-gradient(180deg,#9fb8cf,#566672)" role="img" aria-label="City skyline photo"><span>Location d</span></div>
  <div class="abs loc" style="left:82px;top:72px;background:linear-gradient(180deg,#7f9fbf,#4e6070)" role="img" aria-label="City skyline photo"><span>Location e</span></div>
  <div class="abs loc" style="left:154px;top:72px;background:linear-gradient(180deg,#b3c9de,#6a7987)" role="img" aria-label="City skyline photo"><span>Location f</span></div>
  <div class="footbar"></div>
</section>

<!-- 15 Contact -->
<section class="slide" style="left:951px;top:293px">
  <div class="photo" style="left:0;top:28px;width:222px;height:87px;background:linear-gradient(180deg,#7e8e9c,#3f4c58 60%,#2c3540)" role="img" aria-label="Photo of a city skyline at dusk"></div>
  <div class="abs" style="left:150px;top:0;width:52px;height:125px;background:linear-gradient(180deg,var(--green),var(--blue));opacity:.9"></div>
  <div class="abs" style="left:153px;top:36px;color:#fff;font-size:3.6px;line-height:1.4">Street 1<br>12345 City, Country</div>
  <div class="abs" style="left:153px;top:53px;color:#fff;font-size:3px;line-height:2">
    <div><svg width="4" height="4" viewBox="0 0 4 4"><circle cx="2" cy="2" r="2" fill="#fff"/></svg> +00 00 000000</div>
    <div><svg width="4" height="4" viewBox="0 0 4 4"><circle cx="2" cy="2" r="2" fill="#fff"/></svg> hello@vantorbellway.com</div>
    <div><svg width="4" height="4" viewBox="0 0 4 4"><circle cx="2" cy="2" r="2" fill="#fff"/></svg> www.vantorbellway.com</div>
  </div>
</section>

</main>
</body>
</html>
```